Quorvane Capital Modern Business Card

We need a modern business card template designed for Quorvane Capital.
Quorvane Capital is a diversified global cryptocurrency investment fund.

The font under the logo: Hiragino Kaku Gothic Pro

Color Hexcode: Main colors white (ffffff) & teal (188383), we are open to adding #fcca46 as an accent

Target Market(s)

Accredited Investors, high net worth individuals and institutional investors

Industry/Entity Type

Investment

Contact Information for Business Card

Contact Information should contain
Name
main phone +1 720 555 0147
cell
email

Font styles to use
Sans Serif
Other font styles liked:
• Hiragino Kaku Gothic Pro

Requirements
Must have
• would like to have icons that identify the contact information
• include our website: www.quorvanecapital.example
• include our Tagline: Diversified Crypto Investment Funds
Nice to have
• Would like to have a simple back side with the logo (without the words) and plenty of space

```html
<!DOCTYPE html>
<html lang="en">
<head>
<meta charset="utf-8">
<title>Quorvane Capital — Business Card</title>
<link rel="stylesheet" href="https://fonts.googleapis.com/css2?family=Noto+Sans+JP:wght@400;500&family=Source+Sans+3:wght@400&display=swap">
<style>
  :root {
    --teal: #1f9393;
    --teal-dark: #188383;
    --white: #ffffff;
    --ink: #1d1d1d;
    --backdrop: #e6e6e6;
  }
  * { margin: 0; padding: 0; box-sizing: border-box; }
  html, body { width: 1200px; height: 1000px; overflow: hidden; }
  body { background: var(--backdrop); position: relative; font-family: "Noto Sans JP", sans-serif; }

  .card { position: absolute; overflow: hidden; }

  /* Back side */
  .card-back { left: 170px; top: 112px; width: 590px; height: 338px; background: var(--teal); }
  .card-back .frame {
    position: absolute; left: 30px; top: 31px; width: 528px; height: 272px;
    border: 2px solid var(--white);
    display: flex; align-items: center; justify-content: center;
  }
  .card-back .brand-name {
    color: var(--white); font-family: "Noto Sans JP", sans-serif; font-weight: 500;
    font-size: 26px; letter-spacing: 4px; text-transform: uppercase;
  }

  /* Front side */
  .card-front { left: 390px; top: 558px; width: 600px; height: 342px; background: var(--white); }
  .person-name {
    position: absolute; left: 34px; top: 94px;
    font-size: 27px; font-weight: 400; letter-spacing: 2.5px; color: var(--teal);
  }
  .brand-block { position: absolute; left: 300px; top: 40px; width: 290px; text-align: center; }
  .brand-block .mark-square { width: 22px; height: 22px; background: var(--teal); margin: 30px auto 14px; }
  .brand-block .brand-name {
    font-size: 11px; letter-spacing: 0.3px; color: var(--ink); text-transform: uppercase; line-height: 1;
    margin-left: -52px;
  }
  .brand-block .tagline {
    font-family: "Source Sans 3", sans-serif; font-size: 15.5px; color: var(--teal); margin-top: 8px; margin-left: -34px;
  }
  .divider { position: absolute; left: 0; top: 169px; width: 600px; height: 2px; background: var(--teal); }

  .contact-list { position: absolute; left: 68px; top: 198px; list-style: none; }
  .contact-list li { display: flex; align-items: center; height: 32px; }
  .contact-list svg { width: 24px; height: 20px; margin-right: 22px; fill: var(--teal); }
  .contact-list span { font-size: 20px; letter-spacing: 1.6px; color: var(--teal); }

  .web-band { position: absolute; right: 0; bottom: 0; width: 276px; height: 54px; }
  .web-band svg { position: absolute; inset: 0; }
  .web-band .url {
    position: absolute; left: 50px; top: 15px;
    font-family: "Source Sans 3", sans-serif; font-size: 16.5px; color: var(--white); white-space: nowrap;
  }
</style>
</head>
<body>

<section class="card card-back" aria-label="Card back">
  <div class="frame">
    <span class="brand-name">Quorvane Capital</span>
  </div>
</section>

<section class="card card-front" aria-label="Card front">
  <h1 class="person-name">Name of Person</h1>

  <div class="brand-block">
    <div class="mark-square"></div>
    <p class="brand-name">Quorvane Capital</p>
    <p class="tagline">Diversified Crypto Investment Funds</p>
  </div>

  <div class="divider"></div>

  <ul class="contact-list">
    <li>
      <svg viewBox="0 0 24 20" aria-hidden="true">
        <path d="M2 6 C2 2 22 2 22 6 L22 8 L17 8 L17 5.5 L7 5.5 L7 8 L2 8 Z"/>
        <path d="M7 9 L17 9 L21 18 L3 18 Z"/>
        <circle cx="12" cy="13" r="2.6" fill="#fff"/>
      </svg>
      <span>+1 720 555 0147</span>
    </li>
    <li>
      <svg viewBox="0 0 24 20" aria-hidden="true">
        <path d="M6 1 L9 5 L7.5 7.5 C9 10.5 11 12.5 13.5 14 L16 12.5 L20 15.5 L18 19 C10 18 4 11 3.5 3 Z"/>
      </svg>
      <span>+ 0 000 000 0000</span>
    </li>
    <li>
      <svg viewBox="0 0 24 20" aria-hidden="true">
        <path d="M3 4 L21 4 L12 11 Z"/>
        <path d="M3 6 L12 13 L21 6 L21 16 L3 16 Z"/>
      </svg>
      <span>name@quorvanecapital.example</span>
    </li>
  </ul>

  <div class="web-band">
    <svg viewBox="0 0 276 54" preserveAspectRatio="none" aria-hidden="true">
      <path d="M0 54 C14 30 24 2 62 0 L276 0 L276 54 Z" fill="var(--teal)"/>
    </svg>
    <span class="url">www.quorvanecapital.example</span>
  </div>
</section>

</body>
</html>
```